International Property Consultancy

Brief Overview:

I need a dynamic and well designed website that is easy to use and understand. It has to be unique and different to generic templates that most websites seem to be these days. PLEASE NO GENERIC TEMPLATES FROM THE INTERNET.

Our business has 10 years experience working on struggling international developments that we then work in-house for to turn around and brings bout success. We stay within a project often for long periods of time until success is achieved. We are unique in our approach and completely different to the standard routes to market for many developments. The site is for developers to see what we have done in regards to previous projects, as such we want to incorporate video into this site with a strong design aesthetic. There will be videos of the past projects we have worked on, which will act as case studies.

I like very simple but punchy websites, that people can navigate and understand very easily. Also a big fan of unique and well thought out design aesthetic.

Initial Site layout thoughts:

1) Homepage:
2) About Us
3) What we've done / Work
This part has the projects we have worked on (France, Portugal, London, Morocco). Each one will have some video content and photo images, but also would be good to have a succinct way to mention what we did and the successes in a clever and punchy way.

4) Contact Us

* This is just a guideline. Would be open to input and creative direction on your own part.

*More details and websites we like can be seen in the brief doc attached.

PLEASE VIEW THE WIREFRAME WORD DOC ATTACHED.

Here there are also some more examples to help:

Here are just a few examples of websites and what I like about them:

- www.velmoro.com (clean, nice geometric design aesthetic, good animation when loading and changing pages well thought out all though also coulee be considered a bit dull and basic after the initial homepage slide)
- https://www.farbridgehub.net (Clean site, quite clinical, lacks video content and doesn't engage greatly).
- https://ruskotile.com (minimal, and like how it mixes the design aesthetic more with video and photo content)

- https://www.amberquillworks.com (like the layout of this and how it displays the projects and work section)

- https://brisk.com (Good use of video content)

- https://loomfield.studio (minimal to the point and mixes design with video and animation etc...)

Here is another couple of cool websites that may help give you some direction: https://halvenquay.com www.brisk.com

Hi there, One of the things I thought would be good on the homepage is to add the logo with a 'digital landscape' before flicking down into a slide with video content of the projects... Just an idea but have posted some pics in the brief. We would get this animated for the site. But if you have better ideas, please do run with them. Thanks,

Target Market(s)

Property developers

Number of Pages Required

4 page

Font styles to use
Other font styles liked:
• Read brief

Requirements
Must have
• Needs to be clean, dynamic and easy to follow on desktop and mobile. We will use it as a kind of portfolio website so will need to embed video of past projects we have worked on.

Read brief in docs.
Nice to have
• Clean
Should not have
• Not be another generic template website.
Not have random property stock photos. (We are not a property agency).

```html
<!DOCTYPE html>
<html lang="en">
<head>
<meta charset="utf-8">
<title>Veltarra — International Property Developments</title>
<link rel="stylesheet" href="https://fonts.googleapis.com/css2?family=Nunito:wght@400;600;700;800&display=swap">
<style>
:root{
  --ink:#131c22;
  --night:#111b21;
  --paper:#ffffff;
  --accent:#e39a74;
  --accent-soft:#f6d9c8;
  --muted:#9aa3a8;
  --text-light:#e9ecee;
}
*{box-sizing:border-box;margin:0;padding:0}
html,body{width:1200px;height:3432px;overflow:hidden}
body{font-family:"Nunito",sans-serif;color:var(--ink);background:var(--paper)}
.section{position:relative;width:1200px;overflow:hidden}
.site-nav{position:absolute;top:36px;left:220px;right:210px;display:flex;justify-content:space-between;align-items:center}
.brand{font-weight:800;font-size:26px;letter-spacing:-0.5px}
.nav-links{display:flex;gap:22px;font-size:14px;font-weight:700;list-style:none}
.nav-links .active{color:var(--accent)}
.on-dark{color:var(--text-light)}
.hero{height:700px}
.hero-title{position:absolute;left:220px;top:150px;font-size:46px;line-height:1.12;font-weight:800;width:700px}
.landscape{position:absolute;left:0;top:260px;width:1200px;height:380px;background:linear-gradient(180deg,rgba(255,255,255,0) 0%,var(--accent-soft) 45%,rgba(255,255,255,0) 100%);opacity:.8}
.scroll-cue{position:absolute;left:1030px;top:490px;display:flex;flex-direction:column;align-items:center;gap:10px}
.scroll-cue span{writing-mode:vertical-rl;font-size:12px;font-weight:700;letter-spacing:2px}
.photo-band{height:652px;background:linear-gradient(180deg,#c9cdd0 0%,#9aa0a3 45%,#6b625a 75%,#4a5256 100%)}
.intro{height:760px;background:var(--night)}
.intro-text{position:absolute;left:220px;top:160px;width:740px;color:var(--text-light);font-size:20px;line-height:1.55}
.text-link{position:absolute;font-size:14px;font-weight:700;color:var(--accent);text-decoration:underline}
.slide{position:absolute;top:308px;height:340px}
.slide-main{left:240px;width:720px;background:linear-gradient(180deg,#7e88a8 0%,#b9a6b5 55%,#5c5570 100%)}
.slide-prev{left:0;width:120px;background:linear-gradient(180deg,#cfd4d8,#7d8890)}
.slide-next{left:1080px;width:120px;background:linear-gradient(180deg,#9db0c4,#6f7b4a)}
.slide-label{position:absolute;top:456px;color:#fff;font-size:42px;font-weight:800}
.slider-arrow{position:absolute;top:692px}
.about{height:688px;background:linear-gradient(135deg,#fff 0%,#fff6f1 50%,#fff 100%)}
.about-text{position:absolute;left:220px;top:168px;width:580px;font-size:18px;line-height:1.6}
.about-text p+p{margin-top:24px}
.stat{position:absolute;left:880px}
.stat-value{font-size:56px;font-weight:800;line-height:1}
.stat-label{font-size:14px;margin-top:6px;line-height:1.3}
.contact{height:632px;background:var(--night);color:var(--text-light)}
.contact-title{position:absolute;left:220px;top:196px;font-size:48px;font-weight:800}
.contact-email{position:absolute;left:220px;top:284px;font-size:15px;text-decoration:underline}
.contact-lead{position:absolute;left:604px;top:222px;width:420px;font-size:26px;line-height:1.3}
.contact-note{position:absolute;left:604px;top:326px;font-size:15px;color:var(--muted)}
.site-footer{position:absolute;left:220px;right:210px;top:540px;display:flex;justify-content:space-between;align-items:center;font-size:12px;color:var(--muted)}
.site-footer a{color:var(--text-light);text-decoration:underline}
.social{display:flex;gap:16px}
.social span{width:14px;height:14px;border-radius:50%;background:var(--text-light)}
</style>
</head>
<body>

<section class="section hero">
  <nav class="site-nav">
    <div class="brand">veltarra.</div>
    <ul class="nav-links"><li class="active">Home</li><li>Work</li><li>About</li><li>Contact</li></ul>
  </nav>
  <h1 class="hero-title">Fulfillment of international property developments</h1>
  <div class="landscape" role="img" aria-label="Wireframe digital landscape of rolling peaks"></div>
  <div class="scroll-cue">
    <span>SCROLL</span>
    <svg width="12" height="40" viewBox="0 0 12 40"><path d="M6 0V38M1 33l5 5 5-5" fill="none" stroke="#131c22" stroke-width="1.5"/></svg>
  </div>
</section>

<section class="section photo-band" role="img" aria-label="City riverside with clock tower and bridge under a cloudy sky"></section>

<section class="section intro">
  <nav class="site-nav on-dark">
    <div class="brand">veltarra.</div>
    <ul class="nav-links"><li>Home</li><li class="active">Work</li><li>About</li><li>Contact</li></ul>
  </nav>
  <p class="intro-text">We deliver a unique and truly bespoke approach to delivering international developments to market, with over 10 years success around the world.</p>
  <a class="text-link" style="left:220px;top:236px">See our work</a>
  <div class="slide slide-prev" role="img" aria-label="London project bridge view"></div>
  <div class="slide slide-main" role="img" aria-label="France project: iron tower at dusk"></div>
  <div class="slide slide-next" role="img" aria-label="Morocco project landscape"></div>
  <div class="slide-label" style="left:212px">France</div>
  <div class="slide-label" style="left:1046px">Morocco</div>
  <svg class="slider-arrow" style="left:244px" width="24" height="16" viewBox="0 0 24 16"><path d="M23 8H2M7 3L2 8l5 5" fill="none" stroke="#e9ecee" stroke-width="1.5"/></svg>
  <svg class="slider-arrow" style="left:930px" width="24" height="16" viewBox="0 0 24 16"><path d="M1 8h21M17 3l5 5-5 5" fill="none" stroke="#e9ecee" stroke-width="1.5"/></svg>
</section>

<section class="section about">
  <nav class="site-nav">
    <div class="brand">veltarra.</div>
    <ul class="nav-links"><li>Home</li><li>Work</li><li class="active">About</li><li>Contact</li></ul>
  </nav>
  <div class="about-text">
    <p>We fulfill international property developments in a truly unique way. We've worked on projects around the world taking developments from fields to award winning resorts, and tired underachieving developments to overachieving goliaths.</p>
    <p>By creating a unique and bespoke in-house white-label strategy that allows each project to be the only beneficiary of the work we do.</p>
  </div>
  <div class="stat" style="top:184px"><div class="stat-value">30+</div><div class="stat-label">Members</div></div>
  <div class="stat" style="top:324px"><div class="stat-value">10</div><div class="stat-label">Years<br>in Business</div></div>
  <a class="text-link" style="left:220px;top:556px">About Veltarra</a>
</section>

<section class="section contact">
  <nav class="site-nav on-dark">
    <div class="brand">veltarra.</div>
    <ul class="nav-links"><li>Home</li><li>Work</li><li>About</li><li class="active">Contact</li></ul>
  </nav>
  <h2 class="contact-title">Let's Talk</h2>
  <a class="contact-email">info@veltarra.com</a>
  <p class="contact-lead">Let's build something awesome together!</p>
  <p class="contact-note">Reach out to us and we'll get back to you.</p>
  <a class="text-link" style="left:604px;top:376px">Work with us</a>
  <footer class="site-footer">
    <div>© 2020 Veltarra. All rights reserved. <a>Privacy Policy</a></div>
    <div class="social" aria-label="Social links"><span></span><span></span><span></span></div>
  </footer>
</section>

</body>
</html>
```